Luxury Customizable Mattress Company Needs a Business Card that WOWs

I need a unique business card design that makes people stop... look and think WOW.

We are a new mattress company with our very own line of customizable beds (mattress & base) called the Tessera Bed. The innovation of our mattress is that the entire product is built of smaller components... once put together its a complete bed. It can be cleaned from the inside out. And it's a mattress made to share with a partner. As people's sleep needs are different, one person may prefer a water bed and a softer mattress while their partner may prefer a warm memory foam mattress with a firmer feel. Now they dont need to compromise, as the Tessera Bed allows each sleeper to get exactly what they need. And they can each change the feel of their side of the bed anytime with a click of a button.
check www.Tesserabed-demo.com for more info (some pages do not work) Also check out our Plenix and Clipvane videos.

We also opened up a new facility where people can try out our beds... called the Quill Lounge. This is a secondary business but we would like to have a small logo on the TB business card to highlight it. (quilllounge-demo.com)

Content on card....
Logo: Tessera Bed logo
Name: Mirela Oshwin
Title: CEO & Sleep Enthusiast
Address: 4829 Talbrook Drive Mississauga ON L7X 3K2 Canada
Telephone: 416.555.0193 (place holder .. this # will change)
Email: mirela@tesserabed-demo.com
Web: www.tesserabed-demo.com

Small Logo: Quill Lounge Logo
web: quilllounge-demo.com

Design: bold and modern, the design has a concept, if possible a card people can use (to ensure they keep the card) Ie. Sleep positions or NFC chip or something interesting. I am open to ideas and printing on unique materials... like soft vinyl fabric.

Mattress Consumers
Married Couples
Couples

Health And Wellness

Logo: Tessera Bed logo
Name: Mirela Oshwin
Web: www.tesserabed-demo.com

SMALL Logo: Quill Lounge Logo
web: quilllounge-demo.com

• bold and modern, the design has a concept, if possible a card people can use (to ensure they keep the card)
• ** I LIKE THIS CONCEPT: http://example-cardgallery.test/uploads/2014/04/creative-business-card-sample-18.jpg
• And the DESIGN I thought of has a silhouette of a woman sleeping on top of front of card and if you flip the card over there's a silhouette of a man sleeping on the bottom of the back of the card. IF you put 2 cards together (back to front) it looks like they are sleeping together.
• INSIDE pull out card can be designed later.
• See our website and videos for images we've used in the past.
• We are open to new concepts, images, stories.
• Must be story / people driven. Mattress sales are driven by the idea of good sleep, solving sleep issues and making people happy.
• Just some examples.... adding a feature to the card like a Sleep positions chart or NFC chip or something interesting. I am open to ideas and printing on unique materials... like soft vinyl fabric.
• not dull in colour or concept

```html
<!DOCTYPE html>
<html lang="en">
<head>
<meta charset="utf-8">
<title>Tessera Bed – Business Card</title>
<link rel="stylesheet" href="https://fonts.googleapis.com/css2?family=Arimo&family=Dancing+Script:wght@500&display=swap">
<style>
  :root {
    --page: #ffffff;
    --silver-light: #d9d9d9;
    --silver-mid: #bdbdbd;
    --silver-dark: #a9a9a9;
    --spot: #ffffff;
    --ink: #111111;
    --brand-ink: #5e2f2f;
  }
  html, body {
    margin: 0;
    width: 1200px;
    height: 1200px;
    overflow: hidden;
    background: var(--page);
  }
  .canvas { position: relative; width: 1200px; height: 1200px; }
  .card { position: absolute; display: block; }
  .card--front { left: 51px; top: 135px; width: 767px; height: 438px; }
  .card--back  { left: 380px; top: 654px; width: 768px; height: 438px; }
  .card-spot { fill: var(--spot); }
  .holder-name {
    font-family: "Dancing Script", cursive;
    font-weight: 500;
    fill: var(--ink);
  }
  .brand-name {
    font-family: "Arimo", sans-serif;
    fill: var(--brand-ink);
  }
  .card-title, .contact-label, .contact-value {
    font-family: "Arimo", sans-serif;
    fill: var(--ink);
  }
</style>
</head>
<body>
<div class="canvas">

  <svg class="card card--front" viewBox="0 0 960 548" preserveAspectRatio="none" aria-label="Card front">
    <defs>
      <linearGradient id="brushed-silver-front" x1="0" y1="0" x2="1" y2="0">
        <stop offset="0" stop-color="var(--silver-mid)"/>
        <stop offset="0.12" stop-color="var(--silver-light)"/>
        <stop offset="0.25" stop-color="var(--silver-mid)"/>
        <stop offset="0.4" stop-color="var(--silver-dark)"/>
        <stop offset="0.55" stop-color="var(--silver-light)"/>
        <stop offset="0.7" stop-color="var(--silver-mid)"/>
        <stop offset="0.85" stop-color="var(--silver-light)"/>
        <stop offset="1" stop-color="var(--silver-dark)"/>
      </linearGradient>
    </defs>
    <rect class="card-surface" width="960" height="548" fill="url(#brushed-silver-front)"/>
    <path class="card-spot" d="M290 36 C420 30 515 90 550 250 L581 416 C500 470 400 528 280 520 C120 510 20 400 22 270 C25 130 140 40 290 36 Z"/>
    <text class="brand-name" x="270" y="290" font-size="54" text-anchor="middle">Tessera Bed</text>
    <text class="holder-name" x="392" y="215" font-size="165" textLength="450" lengthAdjust="spacingAndGlyphs">Mirela</text>
    <text class="holder-name" x="396" y="400" font-size="165" textLength="540" lengthAdjust="spacingAndGlyphs">Oshwin</text>
  </svg>

  <svg class="card card--back" viewBox="0 0 960 548" preserveAspectRatio="none" aria-label="Card back">
    <defs>
      <linearGradient id="brushed-silver-back" x1="0" y1="0" x2="1" y2="0">
        <stop offset="0" stop-color="var(--silver-light)"/>
        <stop offset="0.15" stop-color="var(--silver-mid)"/>
        <stop offset="0.3" stop-color="var(--silver-dark)"/>
        <stop offset="0.45" stop-color="var(--silver-light)"/>
        <stop offset="0.6" stop-color="var(--silver-mid)"/>
        <stop offset="0.78" stop-color="var(--silver-dark)"/>
        <stop offset="1" stop-color="var(--silver-light)"/>
      </linearGradient>
    </defs>
    <rect class="card-surface" width="960" height="548" fill="url(#brushed-silver-back)"/>
    <path class="card-spot" d="M505 407 L600 230 C640 160 710 120 780 122 C870 125 920 200 920 300 C920 420 830 487 720 485 C640 483 570 440 505 407 Z"/>
    <text class="brand-name" x="740" y="315" font-size="42" text-anchor="middle">Tessera Bed</text>

    <text class="card-title" x="497" y="92" font-size="48" text-anchor="middle">CEO &amp; Sleep Enthusiant</text>

    <text class="contact-label" x="10" y="197" font-size="30">Address:</text>
    <text class="contact-value" x="162" y="199" font-size="30">4829 Talbrook Drive</text>
    <text class="contact-value" x="162" y="248" font-size="30">Mississauga ON L7X</text>
    <text class="contact-value" x="162" y="297" font-size="30">3K2 Canada</text>

    <text class="contact-label" x="8" y="404" font-size="30">Telephone:</text>
    <text class="contact-value" x="190" y="408" font-size="31">416.555.0193</text>

    <text class="contact-label" x="10" y="472" font-size="28">Email:</text>
    <text class="contact-value" x="100" y="472" font-size="28">mirela@tesserabed-demo.com</text>

    <text class="contact-label" x="8" y="532" font-size="28">Website:</text>
    <text class="contact-value" x="140" y="535" font-size="28">www.tesserabed-demo.com</text>
  </svg>

</div>
</body>
</html>
```